New Therapist Looking for Unique Fun Exciting Brochure for Private Practice

I need a basic brochure displaying my services for my new therapy/counseling business. My company is Stone and Brook PLLC and I would like something that looks earthy with green colors similar to my logo. I want just my logo and my name on the front. I would like a few pictures throughout that include trees and I have added them as uploads. I want it simple, playful and earthy with just my services, business details, my prices, qualifications, mission statement and maybe a quote. I am very authentic and want it to really represent me.

I offer mental health and substance abuse counseling for ages 14 and up. I also do body based work like yoga, breath and medication in my practice.

Will provide text content to winner - please use place holders for now.

Target Market(s)

Behavioral Health hospitals, psychiatrists, doctors, medical professionals, other therapists, substance use treatment centers, holistic practitioners

Industry/Entity Type

Counseling

Font styles to use
Serif

Colors
61bae0
85cae6
9bcb3c
abd037
cadf82
f68e4e
00a990
fbf289

Requirements
Must have
• An authentic feel, earthy and inviting - must include at least one tree picture that I included and my logo, must include one of my profile pictures
Nice to have
• Open - maybe greens and earthy tones similar to my logo
Should not have
• open

```html
<!DOCTYPE html>
<html lang="en">
<head>
<meta charset="utf-8">
<title>Stone and Brook PLLC Brochure</title>
<link href="https://fonts.googleapis.com/css2?family=Montserrat:wght@600;700;800&family=Open+Sans:wght@400;600&display=swap" rel="stylesheet">
<style>
  :root {
    --bg: #ecebe8;
    --paper: #ffffff;
    --green: #5aa63c;
    --green-deep: #2f7d3a;
    --orange: #f68e4e;
    --yellow: #f6c343;
    --text: #5d5d5d;
    --muted: #8a8a8a;
  }
  * { box-sizing: border-box; margin: 0; padding: 0; }
  html, body { width: 1200px; height: 2792px; overflow: hidden; }
  body { background: var(--bg); font-family: "Open Sans", sans-serif; color: var(--text); position: relative; }

  .spread { position: absolute; left: 50px; width: 1100px; height: 778px; background: var(--paper); overflow: hidden; box-shadow: 0 10px 30px rgba(0,0,0,.12); }
  .spread-outer { top: 518px; }
  .spread-inner { top: 1496px; }
  .spread-art { position: absolute; inset: 0; }
  .page { position: absolute; top: 0; width: 550px; height: 778px; }
  .page-left { left: 0; }
  .page-right { left: 550px; }
  .fold { position: absolute; left: 549px; top: 0; width: 2px; height: 778px; background: rgba(0,0,0,.06); }

  /* Back cover */
  .back-brand { position: absolute; left: 40px; top: 560px; display: flex; align-items: center; gap: 10px; }
  .brand-dot { border-radius: 50%; background: var(--green); }
  .back-brand .brand-dot { width: 16px; height: 16px; }
  .back-brand .brand-name { font-family: "Montserrat", sans-serif; font-weight: 700; font-size: 22px; color: var(--green); }
  .contacts { position: absolute; left: 40px; top: 620px; list-style: none; }
  .contact { display: flex; align-items: center; gap: 12px; font-size: 14px; color: var(--text); margin-bottom: 12px; }
  .contact-icon { width: 24px; height: 24px; flex: none; }

  /* Front cover */
  .cover-photo { position: absolute; left: 40px; top: 150px; width: 380px; height: 380px; border-radius: 50%;
    background: linear-gradient(180deg, #c9dcc0 0%, #7fa86a 35%, #4d7a3c 65%, #6b5a3a 100%); }
  .front-brand { position: absolute; right: 40px; top: 44px; display: flex; align-items: center; gap: 10px; }
  .front-brand .brand-dot { width: 18px; height: 18px; }
  .front-brand .brand-name { font-family: "Montserrat", sans-serif; font-weight: 700; font-size: 28px; color: var(--green); }
  .cover-name { position: absolute; right: 40px; top: 545px; text-align: right; font-family: "Montserrat", sans-serif; font-weight: 800; font-size: 44px; line-height: 1.05; color: var(--green); }
  .cover-role { position: absolute; right: 40px; top: 648px; font-family: "Montserrat", sans-serif; font-weight: 600; font-size: 15px; color: var(--orange); }
  .cover-web { position: absolute; right: 40px; top: 720px; font-size: 14px; color: var(--muted); letter-spacing: 1px; }

  /* Inside */
  .section-title { position: absolute; left: 40px; font-family: "Montserrat", sans-serif; font-weight: 800; font-size: 24px; color: var(--orange); letter-spacing: 1px; }
  .section-sub { position: absolute; left: 40px; font-family: "Montserrat", sans-serif; font-weight: 600; font-size: 14px; color: var(--green); }
  .services { position: absolute; left: 40px; right: 40px; top: 400px; list-style: none; }
  .service { display: flex; justify-content: space-between; gap: 20px; margin-bottom: 28px; }
  .service-name { font-family: "Montserrat", sans-serif; font-weight: 700; font-size: 15px; color: var(--green); margin-bottom: 4px; }
  .service-desc { font-size: 12px; line-height: 1.5; color: var(--muted); }
  .service-price { font-family: "Montserrat", sans-serif; font-weight: 700; font-size: 14px; color: var(--orange); white-space: nowrap; padding-top: 2px; }
  .details { position: absolute; left: 40px; right: 40px; top: 405px; }
  .details p { font-size: 12px; line-height: 1.6; color: var(--muted); margin-bottom: 14px; }
</style>
</head>
<body>

<section class="spread spread-outer">
  <svg class="spread-art" viewBox="0 0 1100 778" width="1100" height="778" aria-hidden="true">
    <circle cx="780" cy="340" r="205" fill="none" stroke="var(--orange)" stroke-width="12" stroke-dasharray="420 900" stroke-dashoffset="150"/>
    <circle cx="780" cy="340" r="224" fill="none" stroke="var(--yellow)" stroke-width="4" stroke-dasharray="330 1100" stroke-dashoffset="110"/>
  </svg>

  <div class="page page-left">
    <div class="back-brand"><span class="brand-dot"></span><span class="brand-name">Stone and Brook</span></div>
    <ul class="contacts">
      <li class="contact">
        <svg class="contact-icon" viewBox="0 0 24 24" aria-hidden="true"><circle cx="12" cy="12" r="12" fill="var(--green)"/><path d="M8.5 6.5l2 2-1.2 1.5c.8 1.7 2 2.9 3.7 3.7l1.5-1.2 2 2-1.3 1.8c-3.8-.4-7.1-3.7-7.5-7.5z" fill="#fff"/></svg>
        <span>(555) 014-2938</span>
      </li>
      <li class="contact">
        <svg class="contact-icon" viewBox="0 0 24 24" aria-hidden="true"><circle cx="12" cy="12" r="12" fill="var(--green)"/><rect x="6.5" y="8" width="11" height="8" fill="none" stroke="#fff" stroke-width="1.4"/><path d="M6.5 8l5.5 4.5L17.5 8" fill="none" stroke="#fff" stroke-width="1.4"/></svg>
        <span>hello@stoneandbrook.com</span>
      </li>
      <li class="contact">
        <svg class="contact-icon" viewBox="0 0 24 24" aria-hidden="true"><circle cx="12" cy="12" r="12" fill="var(--green)"/><circle cx="12" cy="12" r="5.5" fill="none" stroke="#fff" stroke-width="1.4"/><path d="M6.5 12h11M12 6.5c-2.5 3-2.5 8 0 11M12 6.5c2.5 3 2.5 8 0 11" fill="none" stroke="#fff" stroke-width="1.2"/></svg>
        <span>www.stoneandbrook.com</span>
      </li>
    </ul>
  </div>

  <div class="page page-right">
    <div class="front-brand"><span class="brand-dot"></span><span class="brand-name">Stone and Brook</span></div>
    <div class="cover-photo" role="img" aria-label="Photograph of tall trees in a sunlit forest"></div>
    <h1 class="cover-name">MAREN<br>ASHBY</h1>
    <p class="cover-role">Licensed Professional Counselor</p>
    <p class="cover-web">www.stoneandbrook.com</p>
  </div>
  <div class="fold"></div>
</section>

<section class="spread spread-inner">
  <svg class="spread-art" viewBox="0 0 1100 778" width="1100" height="778">
    <defs>
      <linearGradient id="portraitTone" x1="0" y1="0" x2="1" y2="1">
        <stop offset="0" stop-color="#3b3530"/>
        <stop offset="0.5" stop-color="#6e5a4a"/>
        <stop offset="1" stop-color="#a58a72"/>
      </linearGradient>
      <linearGradient id="leafBand" x1="0" y1="0" x2="1" y2="1">
        <stop offset="0" stop-color="#2f7d3a"/>
        <stop offset="0.6" stop-color="#4f9e3c"/>
        <stop offset="1" stop-color="#8cc24a"/>
      </linearGradient>
    </defs>
    <g role="img" aria-label="Portrait photograph of the counselor">
      <path d="M0 0 H550 V235 C420 310 200 300 0 245 Z" fill="url(#portraitTone)"/>
    </g>
    <path d="M0 262 C180 330 400 330 550 238" fill="none" stroke="var(--orange)" stroke-width="10"/>
    <path d="M0 284 C200 352 420 348 550 264" fill="none" stroke="var(--yellow)" stroke-width="4"/>
    <g role="img" aria-label="Green leafy canopy backdrop">
      <path d="M550 0 H1100 V290 C950 245 760 335 550 285 Z" fill="url(#leafBand)"/>
    </g>
    <path d="M550 300 C760 350 950 265 1100 298" fill="none" stroke="var(--orange)" stroke-width="8"/>
    <path d="M550 318 C760 366 950 285 1100 316" fill="none" stroke="var(--yellow)" stroke-width="3"/>
  </svg>

  <div class="page page-left">
    <h2 class="section-title" style="top:335px">OUR SERVICES</h2>
    <p class="section-sub" style="top:368px">Counseling for ages 14 and up</p>
    <ul class="services">
      <li class="service">
        <div><h3 class="service-name">Individual Counseling</h3><p class="service-desc">One-on-one sessions for mental health,<br>stress, anxiety and life changes.</p></div>
        <span class="service-price">$120 / session</span>
      </li>
      <li class="service">
        <div><h3 class="service-name">Substance Use Counseling</h3><p class="service-desc">Support and recovery planning in a<br>safe, caring and open setting.</p></div>
        <span class="service-price">$130 / session</span>
      </li>
      <li class="service">
        <div><h3 class="service-name">Body-Based Practice</h3><p class="service-desc">Gentle yoga, breath work and guided<br>meditation woven into therapy.</p></div>
        <span class="service-price">$90 / session</span>
      </li>
    </ul>
  </div>

  <div class="page page-right">
    <h2 class="section-title" style="top:340px">BUSINESS DETAILS</h2>
    <p class="section-sub" style="top:373px">Welcome to Stone and Brook PLLC</p>
    <div class="details">
      <p>Stone and Brook is a private counseling practice rooted in warmth, honesty and growth. Every session is a calm space to slow down, be heard and find a path forward at your own pace.</p>
      <p>Our mission is to help teens and adults heal mind and body together, blending proven talk therapy with yoga, breath and mindful movement for lasting, grounded change.</p>
      <p>Referrals are welcome from hospitals, physicians, therapists, treatment centers and holistic practitioners. Call or email to book a first visit today.</p>
    </div>
  </div>
  <div class="fold"></div>
</section>

</body>
</html>
```